Harlow Grading LLC business card design

Excavation company business cards

Contact Information for Business Card

Harlow Grading LLC cell phone 208-471-9360 office phone 208-396-4815 harlowgradingllc@mailverde.net Driveways, site prep, retaining walls, septic systems, rock delivery

Colors

Designer to choose colors to be used in the design.

```html
<!DOCTYPE html>
<html lang="en">
<head>
<meta charset="utf-8">
<title>Harlow Grading LLC – Business Card</title>
<link href="https://fonts.googleapis.com/css2?family=Montserrat:wght@400;500;800&display=swap" rel="stylesheet">
<style>
  :root {
    --page-bg: #e9e7e4;
    --card-white: #ffffff;
    --card-black: #141414;
    --brand-orange: #ec6a22;
    --ink-grey: #555555;
    --emboss: #262626;
  }
  * { margin: 0; padding: 0; box-sizing: border-box; }
  html, body { width: 1200px; height: 912px; overflow: hidden; }
  body {
    background: var(--page-bg);
    font-family: "Montserrat", sans-serif;
    display: flex; flex-direction: column; align-items: center; justify-content: center;
    gap: 36px;
  }
  .card {
    width: 700px; height: 400px; position: relative; overflow: hidden;
    box-shadow: 0 6px 18px rgba(0,0,0,.18);
  }
  .card-back { background: var(--card-black); display: flex; align-items: center; justify-content: center; }
  .back-wordmark {
    color: var(--emboss); font-weight: 800; font-size: 42px; letter-spacing: 2px;
    text-transform: uppercase; display: flex; align-items: center; gap: 18px; white-space: nowrap;
  }
  .back-wordmark .mark-square { width: 32px; height: 32px; background: var(--emboss); flex: none; }
  .card-front { background: var(--card-white); }
  .name-accent { position: absolute; left: 0; top: 98px; width: 20px; height: 44px; background: var(--brand-orange); }
  .holder { position: absolute; left: 46px; top: 96px; }
  .holder-name { color: var(--brand-orange); font-weight: 800; font-size: 24px; letter-spacing: .5px; text-transform: uppercase; line-height: 1.1; white-space: nowrap; }
  .holder-title { color: var(--ink-grey); font-size: 19px; font-weight: 400; margin-top: 2px; }
  .wordmark {
    position: absolute; right: 40px; top: 172px; display: flex; align-items: center; gap: 10px;
    color: var(--brand-orange); font-weight: 800; font-size: 26px; text-transform: uppercase; letter-spacing: 1px;
    white-space: nowrap;
  }
  .wordmark .mark-square { width: 22px; height: 22px; background: var(--brand-orange); flex: none; }
  .contacts { position: absolute; left: 46px; top: 250px; list-style: none; }
  .contacts li { display: flex; align-items: center; gap: 10px; color: var(--ink-grey); font-size: 19px; line-height: 28px; white-space: nowrap; }
  .contacts svg { width: 14px; height: 14px; fill: none; stroke: var(--brand-orange); stroke-width: 2; flex: none; }
  .services-band {
    position: absolute; left: 0; right: 0; bottom: 0; height: 56px; background: var(--brand-orange);
    color: #fff; font-size: 16px; font-weight: 500; display: flex; align-items: center; padding-left: 46px;
    white-space: nowrap;
  }
</style>
</head>
<body>
  <section class="card card-back" aria-label="Card back">
    <div class="back-wordmark"><span class="mark-square"></span>Harlow Grading LLC</div>
  </section>

  <section class="card card-front" aria-label="Card front">
    <span class="name-accent"></span>
    <div class="holder">
      <p class="holder-name">Dale Mercer</p>
      <p class="holder-title">Director</p>
    </div>
    <div class="wordmark"><span class="mark-square"></span>Harlow Grading LLC</div>
    <ul class="contacts">
      <li><svg viewBox="0 0 14 14"><rect x="3.5" y="1" width="7" height="12" rx="1.2"/><line x1="6" y1="11" x2="8" y2="11"/></svg>208-471-9360</li>
      <li><svg viewBox="0 0 14 14"><path d="M2 4c0-1.5 1.5-2 5-2s5 .5 5 2v1H9.5V4h-5v1H2z"/><rect x="2.5" y="6.5" width="9" height="6" rx="1"/></svg>208-396-4815</li>
      <li><svg viewBox="0 0 14 14"><rect x="1" y="3" width="12" height="8" rx="1"/><polyline points="1,3 7,8 13,3"/></svg>harlowgradingllc@mailverde.net</li>
    </ul>
    <div class="services-band">Driveways, | site prep, | retaining walls, | septic systems, | rock delivery</div>
  </section>
</body>
</html>
```